Kelvane Plumbing Business cards

Company is Kelvane Plumbing.
name Dashel Morrowby, I am a plumber, drainer, gasfitter and roofer
Mobile: 0431 906 154
Email address: info@kelvaneplumbing.example (check out my website for some ideas)
Website: www.kelvaneplumbing.example
ABN: 82 916 203 471
LIC: 604517K

I am reliable all round plumber. I am a 24 hour emergency service. Kelvane Plumbing is a professional plumbing service in the Illawarra, South Coast, Southern Sydney and Southern Highland regions of NSW. We offer a 24 hour emergency service for piece of mind to our customers. Call us now to see how we can help you. Kelvane Plumbing approaches every job with attention to detail and excellent customer service. With our superior workmanship you can be confident that the job will be done right the first time around. You can rest assured with results that are guaranteed to last.

Target Market(s)

the general public

Contact Information for Business Card

look up website for some ideas something with similar colours to logo and new modern and to catch the eye.

Colors
fdfdfd
ffffff
000000
7f7f7f
aaaaaa
33a6d7
0492cd

Requirements
Must have
• all contact details
• company- Kelvane Plumbing
• name- Dashel Morrowby
• number mobile- 0431 906 154
• Email address- info@kelvaneplumbing.example
• Website- www.kelvaneplumbing.example
• ABN- 82 916 203 471
• LIC- 604517K

```html
<!DOCTYPE html>
<html lang="en">
<head>
<meta charset="utf-8">
<title>Kelvane Plumbing – Business Cards</title>
<link rel="stylesheet" href="https://fonts.googleapis.com/css2?family=Arimo&family=Questrial&family=Noto+Serif&display=swap">
<style>
  :root {
    --paper: #ffffff;
    --ink: #000000;
    --mist: #f0f0f2;
    --snow: #fdfdfd;
    --brand-blue: #0492cd;
    --steel: #7f7f7f;
  }
  html, body {
    margin: 0;
    width: 1200px;
    height: 1200px;
    overflow: hidden;
    background: var(--paper);
  }
  .canvas {
    position: relative;
    width: 1200px;
    height: 1200px;
  }
  .card {
    position: absolute;
    left: 168px;
    width: 840px;
    height: 480px;
    overflow: hidden;
  }
  .card--front {
    top: 106px;
    background: var(--ink);
  }
  .card--back {
    top: 620px;
    height: 478px;
    background: var(--mist);
  }
  .wordmark {
    position: absolute;
    margin: 0;
    font-family: "Questrial", sans-serif;
    font-weight: 400;
    color: var(--brand-blue);
    white-space: nowrap;
    letter-spacing: 1px;
  }
  .card--front .wordmark {
    left: 0;
    right: 0;
    top: 210px;
    text-align: center;
    font-size: 56px;
    line-height: 60px;
  }
  .back-lower {
    position: absolute;
    left: 0;
    right: 0;
    top: 256px;
    bottom: 0;
    background: var(--ink);
  }
  .brand-panel {
    position: absolute;
    left: 401px;
    top: 83px;
    width: 431px;
    height: 240px;
    background: var(--ink);
    border-radius: 120px 0 0 120px;
  }
  .brand-panel .wordmark {
    left: 40px;
    right: 20px;
    top: 100px;
    text-align: center;
    font-size: 34px;
    line-height: 40px;
  }
  .person-name {
    position: absolute;
    left: 30px;
    top: 60px;
    margin: 0;
    font-family: "Arimo", sans-serif;
    font-weight: 400;
    font-size: 39px;
    line-height: 44px;
    color: var(--ink);
  }
  .person-role {
    position: absolute;
    left: 51px;
    top: 105px;
    margin: 0;
    font-family: "Noto Serif", serif;
    font-size: 12px;
    color: var(--ink);
  }
  .contact-list {
    position: absolute;
    left: 70px;
    top: 308px;
    margin: 0;
    padding: 0;
    list-style: none;
    font-family: "Questrial", sans-serif;
    font-size: 17px;
    color: var(--snow);
  }
  .contact-list li {
    display: flex;
    align-items: center;
    height: 40px;
  }
  .contact-icon {
    width: 24px;
    height: 24px;
    margin-right: 15px;
    flex: none;
  }
  .registration {
    position: absolute;
    right: 16px;
    top: 387px;
    margin: 0;
    text-align: right;
    font-family: "Questrial", sans-serif;
    font-size: 17px;
    line-height: 23px;
    color: var(--snow);
  }
</style>
</head>
<body>
<main class="canvas">
  <section class="card card--front" aria-label="Business card front">
    <h1 class="wordmark">Kelvane Plumbing</h1>
  </section>

  <section class="card card--back" aria-label="Business card back">
    <div class="back-lower"></div>

    <h2 class="person-name">Dashel Morrowby</h2>
    <p class="person-role">Plumber, drainer, gasfitter and roofer</p>

    <div class="brand-panel">
      <p class="wordmark">Kelvane Plumbing</p>
    </div>

    <ul class="contact-list">
      <li>
        <svg class="contact-icon" viewBox="0 0 24 24" aria-hidden="true">
          <path fill="#fdfdfd" d="M6.6 2.5c.5-.3 1.1-.2 1.5.3l2.2 3.1c.4.5.3 1.2-.2 1.6l-1.5 1.1c.9 2.2 2.6 4 4.8 5l1.1-1.5c.4-.5 1.1-.6 1.6-.2l3.1 2.2c.5.4.6 1 .3 1.5l-1.2 2.1c-.5.8-1.4 1.2-2.3 1C9.9 18.4 5.6 14.1 4.3 8c-.2-.9.2-1.8 1-2.3z"/>
        </svg>
        <span>0431 906 154</span>
      </li>
      <li>
        <svg class="contact-icon" viewBox="0 0 24 24" aria-hidden="true">
          <rect x="2" y="6" width="20" height="13" fill="none" stroke="#fdfdfd" stroke-width="1.6"/>
          <path d="M2 6l10 8 10-8M2 19l7.5-7M22 19l-7.5-7" fill="none" stroke="#fdfdfd" stroke-width="1.6"/>
        </svg>
        <span>info@kelvaneplumbing.example</span>
      </li>
      <li>
        <svg class="contact-icon" viewBox="0 0 24 24" aria-hidden="true">
          <g fill="none" stroke="#fdfdfd" stroke-width="1.4">
            <circle cx="12" cy="12" r="10"/>
            <ellipse cx="12" cy="12" rx="4.5" ry="10"/>
            <path d="M2 12h20M4 6.5h16M4 17.5h16M12 2v20"/>
          </g>
        </svg>
        <span>www.kelvaneplumbing.example</span>
      </li>
    </ul>

    <p class="registration">ABN- 82 916 203 471<br>LIC- 604517K</p>
  </section>
</main>
</body>
</html>
```